Business card design for online Mandarin Learning School

We need a business card design for our online language learning school called "Maple Bridge Online for Mandarin Learning". Our existing website is https://www.maplebridgeonline.com
We have our logo already. We would like to see our business card design that can make our online teaching services to be innovative, young, energetic and fun to learn. Prefer to have a certain level of color matching with our website. Apart from "Maple Bridge Online", need to specifically state "for Mandarin Learning" as well on the business card.

```html
<!DOCTYPE html>
<html lang="en">
<head>
<meta charset="utf-8">
<title>Maple Bridge Online – Business Card</title>
<link rel="stylesheet" href="https://fonts.googleapis.com/css2?family=Cinzel:wght@400;500&family=Roboto:wght@500;700&display=swap">
<style>
  :root {
    --teal: #22a6b3;
    --coral: #e05a5c;
    --grey: #737373;
    --ink: #555555;
    --cream: #efefe3;
    --paper: #ffffff;
    --backdrop: #e9edee;
  }
  * { box-sizing: border-box; margin: 0; padding: 0; }
  html, body { width: 1200px; height: 900px; overflow: hidden; }
  body {
    background: var(--backdrop);
    display: flex;
    flex-direction: column;
    align-items: center;
    justify-content: space-evenly;
  }
  .card {
    width: 630px;
    height: 360px;
    background: var(--paper);
    box-shadow: 0 2px 10px rgba(0,0,0,0.08);
    position: relative;
  }

  /* Front */
  .card-front {
    display: flex;
    align-items: center;
    justify-content: center;
    gap: 22px;
  }
  .brand-dot {
    width: 56px; height: 56px;
    border-radius: 50%;
    background: var(--teal);
  }
  .brand-name {
    font-family: "Cinzel", serif;
    font-weight: 400;
    font-size: 48px;
    letter-spacing: 2px;
    color: var(--teal);
  }

  /* Back */
  .card-back { padding: 34px 40px; }
  .name-panel {
    background: var(--cream);
    width: 410px;
    padding: 12px 18px 10px;
  }
  .name-panel .brand-name { font-size: 38px; line-height: 1; display: block; }
  .name-rule { height: 4px; background: var(--grey); margin: 8px 0 6px; }
  .panel-url {
    font-family: "Cinzel", serif;
    font-size: 17px;
    color: var(--coral);
    letter-spacing: 1px;
  }
  .tagline {
    font-family: "Cinzel", serif;
    font-size: 27px;
    color: var(--coral);
    margin: 22px 0 14px;
    letter-spacing: 1px;
  }
  .accent-line { display: flex; height: 4px; }
  .accent-line .seg-coral { flex: 2; background: var(--coral); }
  .accent-line .seg-teal { flex: 2; background: var(--teal); }
  .accent-line .seg-grey { flex: 1.6; background: var(--grey); }

  .contacts {
    display: flex;
    justify-content: space-between;
    margin-top: 26px;
  }
  .contact-list { list-style: none; display: flex; flex-direction: column; gap: 14px; }
  .contact-item {
    display: flex; align-items: center; gap: 14px;
    font-family: "Roboto", sans-serif;
    font-weight: 700;
    font-size: 13px;
    color: var(--ink);
  }
  .contact-list.right .contact-item { flex-direction: row-reverse; text-align: right; }
  .icon { width: 26px; height: 26px; flex: none; fill: var(--teal); }
  .phone-lines { line-height: 1.35; }
</style>
</head>
<body>

<section class="card card-front" aria-label="Card front">
  <span class="brand-dot" aria-hidden="true"></span>
  <span class="brand-name">Maple Bridge</span>
</section>

<section class="card card-back" aria-label="Card back">
  <div class="name-panel">
    <span class="brand-name">Maple Bridge</span>
    <div class="name-rule"></div>
    <div class="panel-url">www.maplebridgeonline.com</div>
  </div>

  <p class="tagline">For Mandarin Learning</p>

  <div class="accent-line" aria-hidden="true">
    <span class="seg-coral"></span><span class="seg-teal"></span><span class="seg-grey"></span>
  </div>

  <div class="contacts">
    <ul class="contact-list left">
      <li class="contact-item">
        <svg class="icon" viewBox="0 0 24 24" aria-hidden="true"><circle cx="12" cy="7" r="5"/><path d="M3 23c0-6 4-9 9-9s9 3 9 9z"/></svg>
        <span>Your Name</span>
      </li>
      <li class="contact-item">
        <svg class="icon" viewBox="0 0 24 24" aria-hidden="true"><path d="M2 5h20v14H2z"/><path d="M2 5l10 8 10-8" fill="none" stroke="#fff" stroke-width="1.6"/></svg>
        <span>Youremail@xyz.com</span>
      </li>
    </ul>
    <ul class="contact-list right">
      <li class="contact-item">
        <svg class="icon" viewBox="0 0 24 24" aria-hidden="true"><circle cx="12" cy="12" r="11"/><g fill="none" stroke="#fff" stroke-width="1.3"><ellipse cx="12" cy="12" rx="5" ry="11"/><path d="M1 12h22M3 6.5h18M3 17.5h18M12 1v22"/></g></svg>
        <span>www.maplebridgeonline.com</span>
      </li>
      <li class="contact-item">
        <svg class="icon" viewBox="0 0 24 24" aria-hidden="true"><path d="M9 2L5 4c-2 5 0 13 5 17l4 1 1-5-3-1c-2-2-3-5-2-8l3-1z"/></svg>
        <span class="phone-lines">000.000.0000<br>000.000.0000</span>
      </li>
    </ul>
  </div>
</section>

</body>
</html>
```